Business cards and stationary design

We just completed the design of our new logo and we need to print new business cards and letterhead for our nonprofit. We are looking for a fresh new design that shows off our new logo. On letterhead, we must have a column on the right or left to include our Board of Directors (up to 45 names) (see attachment)

Industry/Entity Type

Non-Profit

Contact Information for Business Card

Standard business card with name, title, Company name, mailing address phone numbers, email address and website. Tagline on back "Bringing the homeless home"

Font styles to use
Sans Serif

Requirements
Must have
• include pertinent information above
• new logo
• fonts compatible with logo
• should use logo colors only
Nice to have
• tag lines

```html
<!DOCTYPE html>
<html lang="en">
<head>
<meta charset="utf-8">
<title>Haven Rise Center — Business Card</title>
<link rel="stylesheet" href="https://fonts.googleapis.com/css2?family=Michroma&display=swap">
<style>
  :root {
    --teal: #1a9bb8;
    --teal-deep: #0b7f99;
    --red: #e2474f;
    --paper: #f6f6f4;
    --ground: #2a2a2c;
    --white: #ffffff;
  }
  * { box-sizing: border-box; margin: 0; padding: 0; }
  html, body {
    width: 1200px; height: 900px; overflow: hidden;
    background: var(--ground);
    font-family: "Michroma", sans-serif;
  }
  .canvas {
    width: 1200px; height: 900px;
    display: flex; flex-direction: column; align-items: center; justify-content: center;
    gap: 40px;
  }
  .card {
    position: relative;
    width: 700px; height: 400px;
    overflow: hidden;
  }
  /* Front */
  .card-front { background: var(--paper); }
  .brand {
    position: absolute; left: 230px; right: 48px; top: 62px;
    display: flex; align-items: center; gap: 14px;
  }
  .brand-mark { flex: none; width: 20px; height: 20px; background: var(--teal); }
  .brand-name {
    font-size: 21px; letter-spacing: 1.5px; color: var(--teal);
    white-space: nowrap;
  }
  .brand-rule {
    position: absolute; left: 230px; right: 48px; top: 106px; height: 1.5px;
    background: var(--red);
  }
  .person { position: absolute; left: 48px; right: 48px; top: 160px; }
  .person-row { display: flex; align-items: center; gap: 12px; }
  .person-name {
    font-size: 17px; letter-spacing: 1.5px; color: var(--red);
    white-space: nowrap;
  }
  .name-rule { flex: 1; height: 1.5px; background: var(--red); }
  .person-title { font-size: 11px; letter-spacing: 2px; color: var(--teal); margin-top: 6px; }
  .contact {
    position: absolute; left: 48px; top: 230px;
    list-style: none; font-size: 11px; letter-spacing: 1.5px; color: var(--teal);
    line-height: 22px;
  }
  .address {
    position: absolute; right: 48px; bottom: 36px; text-align: right;
    font-style: normal; font-size: 12px; letter-spacing: 2px; color: var(--teal);
    line-height: 22px;
  }
  /* Back */
  .card-back {
    background: radial-gradient(ellipse at 40% 35%, var(--teal) 0%, var(--teal-deep) 100%);
    display: flex; flex-direction: column; align-items: center; justify-content: center;
  }
  .back-mark { width: 30px; height: 30px; background: var(--white); margin-bottom: 28px; }
  .back-name { font-size: 30px; letter-spacing: 3px; color: var(--white); white-space: nowrap; }
  .back-rule { width: 520px; height: 1.5px; background: var(--white); margin: 14px 0 12px; opacity: .85; }
  .back-web { font-size: 12px; letter-spacing: 2px; color: var(--white); }
</style>
</head>
<body>
<main class="canvas">
  <section class="card card-front">
    <div class="brand">
      <span class="brand-mark"></span>
      <span class="brand-name">HAVEN RISE CENTER</span>
    </div>
    <div class="brand-rule"></div>

    <div class="person">
      <div class="person-row">
        <p class="person-name">MARCUS DELAINE</p>
        <span class="name-rule"></span>
      </div>
      <p class="person-title">CHAIRMAN</p>
    </div>

    <ul class="contact">
      <li>555.014.2290</li>
      <li>WWW.HAVENRISECENTER.ORG</li>
      <li>HELLO@HAVENRISECENTER.ORG</li>
    </ul>

    <address class="address">
      P.O. Box 20418,<br>
      Riverton, Ohio 43090
    </address>
  </section>

  <section class="card card-back">
    <span class="back-mark"></span>
    <p class="back-name">HAVEN RISE CENTER</p>
    <div class="back-rule"></div>
    <p class="back-web">WWW.HAVENRISECENTER.ORG</p>
  </section>
</main>
</body>
</html>
```